Rework of existing labels

The task consist of reworking the current attached labels so that they read The Otterwrap Company instead of The Otter Wrap Company. The budget is for the rework of three labels:

- A rectangular label in horizontal in two version, one Spanish and one English, as further described below.
- A rectangular label in vertical, with six different versions to account for different sizes and TOGs
- A round tag label

The font to be used is Univers (also attached)

The current labels along with the corporate manual and the font sample is attached. New labels should not be a big deviating from the style of the current ones. Logo should remain the same.

Requirements
Must have
• Penguin logo should not be changed
• You need to provide:
• Logo to replace logo in files 4 and 5 (one in English one in Spanish)
• Tag label to replace tag in file 3
• Label to replace label in file 6. For this one, once you are selected, you will need to prepare a set of 6 labels, for 6 different combinations of size and tog.
Should not have
• Deviations from current labels so that they appear as of different series

```html
<!DOCTYPE html>
<html lang="en">
<head>
<meta charset="utf-8">
<title>The Otterwrap Company – Label Set</title>
<link rel="stylesheet" href="https://fonts.googleapis.com/css2?family=Roboto+Condensed:wght@400;700&display=swap">
<style>
  :root {
    --green: #8dc63f;
    --orange: #f7941d;
    --orange-soft: #fbb040;
    --paper: #ffffff;
    --rule: #bdbdbd;
  }
  html, body {
    margin: 0;
    padding: 0;
    width: 1200px;
    height: 1000px;
    overflow: hidden;
    background: var(--paper);
  }
  .label-sheet {
    display: block;
    width: 1200px;
    height: 1000px;
    font-family: "Roboto Condensed", "Arial Narrow", sans-serif;
  }
  .set--green  { --ink: var(--green);  --ink-soft: var(--green); }
  .set--orange { --ink: var(--orange); --ink-soft: var(--orange-soft); }

  .lang-heading { fill: var(--ink); font-size: 14px; font-weight: 700; text-anchor: middle; }
  .lang-bracket { fill: none; stroke: var(--ink); stroke-width: 2; }

  .ink-fill  { fill: var(--ink); }
  .soft-fill { fill: var(--ink-soft); }
  .paper-fill { fill: var(--paper); }

  .scallop-ink   { fill: var(--ink); stroke: var(--ink); stroke-linecap: round; }
  .scallop-paper { fill: var(--paper); stroke: var(--paper); stroke-linecap: round; }

  .brand-name { font-weight: 700; letter-spacing: 0.2px; }
  .brand-name--ink   { fill: var(--ink); }
  .brand-name--soft  { fill: var(--ink-soft); }
  .brand-name--paper { fill: var(--paper); }
  .brand-name--center { text-anchor: middle; font-size: 16px; }
  .brand-name--left   { font-size: 18px; }

  .tagline { font-weight: 400; }
  .tagline--round { font-size: 6px; text-anchor: middle; }
  .tagline--rect  { font-size: 9px; text-anchor: middle; }
  .tagline--paper { fill: var(--paper); }
  .tagline--ink   { fill: var(--ink); }
</style>
</head>
<body>
<svg class="label-sheet" viewBox="0 0 1200 1000" xmlns="http://www.w3.org/2000/svg">
  <defs>
    <linearGradient id="divider-fade" x1="0" x2="1" y1="0" y2="0">
      <stop offset="0" stop-color="#bdbdbd" stop-opacity="0"/>
      <stop offset="0.5" stop-color="#a8a8a8"/>
      <stop offset="1" stop-color="#bdbdbd" stop-opacity="0"/>
    </linearGradient>
  </defs>

  <!-- Green set -->
  <g class="set set--green">
    <g class="lang-headings">
      <text class="lang-heading" x="355" y="30">English</text>
      <path class="lang-bracket" d="M263 45 V37 H448 V45"/>
      <text class="lang-heading" x="555" y="30">Spanish</text>
      <path class="lang-bracket" d="M463 45 V37 H648 V45"/>
    </g>

    <!-- Round tag, outlined, English -->
    <g class="round-tag round-tag--outline">
      <circle class="ink-fill" cx="355" cy="147" r="92"/>
      <circle class="scallop-paper" cx="355" cy="147" r="78" stroke-width="14" stroke-dasharray="0 19.6"/>
      <circle class="brand-mark ink-fill" cx="355" cy="112" r="38"/>
      <text class="brand-name brand-name--ink brand-name--center" x="355" y="181">THE OTTERWRAP</text>
      <text class="brand-name brand-name--ink brand-name--center" x="355" y="196">COMPANY</text>
      <rect class="ink-fill" x="307" y="199" width="102" height="9"/>
      <text class="tagline tagline--round tagline--paper" x="358" y="206">Warm sleeping for young kids</text>
    </g>

    <!-- Round tag, outlined, Spanish -->
    <g class="round-tag round-tag--outline">
      <circle class="ink-fill" cx="555" cy="145" r="92"/>
      <circle class="scallop-paper" cx="555" cy="145" r="78" stroke-width="14" stroke-dasharray="0 19.6"/>
      <circle class="brand-mark ink-fill" cx="555" cy="110" r="38"/>
      <text class="brand-name brand-name--ink brand-name--center" x="555" y="179">THE OTTERWRAP</text>
      <text class="brand-name brand-name--ink brand-name--center" x="555" y="194">COMPANY</text>
      <rect class="ink-fill" x="504" y="197" width="102" height="9"/>
      <text class="tagline tagline--round tagline--paper" x="555" y="204">Cálidos sueños, niños felices</text>
    </g>

    <!-- Horizontal label, outlined -->
    <g class="rect-label rect-label--outline">
      <rect class="ink-fill" x="663" y="87" width="277" height="123"/>
      <rect class="scallop-paper" x="678" y="100" width="247" height="97" stroke-width="10" stroke-dasharray="0 12.07"/>
      <text class="brand-name brand-name--ink brand-name--left" x="678" y="130">THE OTTERWRAP</text>
      <text class="brand-name brand-name--ink brand-name--left" x="678" y="147">COMPANY</text>
      <rect class="ink-fill" x="678" y="153" width="150" height="14"/>
      <text class="tagline tagline--rect tagline--paper" x="745" y="163">Cálidos sueños, niños felices</text>
      <circle class="brand-mark ink-fill" cx="875" cy="148" r="36"/>
    </g>

    <!-- Round tag, filled, English -->
    <g class="round-tag round-tag--filled">
      <circle class="scallop-ink" cx="355" cy="358" r="80" stroke-width="20" stroke-dasharray="0 20.94"/>
      <circle class="brand-mark paper-fill" cx="355" cy="325" r="38"/>
      <text class="brand-name brand-name--paper brand-name--center" x="355" y="389">THE OTTERWRAP</text>
      <text class="brand-name brand-name--paper brand-name--center" x="355" y="404">COMPANY</text>
      <rect class="paper-fill" x="305" y="412" width="102" height="9"/>
      <text class="tagline tagline--round tagline--ink" x="356" y="419">Warm sleeping for young kids</text>
    </g>

    <!-- Round tag, filled, Spanish -->
    <g class="round-tag round-tag--filled">
      <circle class="scallop-ink" cx="555" cy="360" r="80" stroke-width="20" stroke-dasharray="0 20.94"/>
      <circle class="brand-mark paper-fill" cx="555" cy="327" r="38"/>
      <text class="brand-name brand-name--paper brand-name--center" x="555" y="391">THE OTTERWRAP</text>
      <text class="brand-name brand-name--paper brand-name--center" x="555" y="406">COMPANY</text>
      <rect class="paper-fill" x="504" y="413" width="102" height="9"/>
      <text class="tagline tagline--round tagline--ink" x="555" y="420">Cálidos sueños, niños felices</text>
    </g>

    <!-- Horizontal label, filled -->
    <g class="rect-label rect-label--filled">
      <rect class="scallop-ink" x="676" y="306" width="251" height="105" stroke-width="12" stroke-dasharray="0 12.07"/>
      <text class="brand-name brand-name--paper brand-name--left" x="678" y="340">THE OTTERWRAP</text>
      <text class="brand-name brand-name--paper brand-name--left" x="678" y="357">COMPANY</text>
      <rect class="paper-fill" x="679" y="363" width="150" height="14"/>
      <text class="tagline tagline--rect tagline--ink" x="746" y="373">Cálidos sueños, niños felices</text>
      <circle class="brand-mark paper-fill" cx="875" cy="358" r="36"/>
    </g>
  </g>

  <!-- Divider -->
  <rect class="set-divider" x="60" y="496" width="1080" height="6" fill="url(#divider-fade)"/>

  <!-- Orange set -->
  <g class="set set--orange" transform="translate(0 532)">
    <g class="lang-headings">
      <text class="lang-heading" x="355" y="30">English</text>
      <path class="lang-bracket" d="M263 45 V37 H448 V45"/>
      <text class="lang-heading" x="555" y="30">Spanish</text>
      <path class="lang-bracket" d="M463 45 V37 H648 V45"/>
    </g>

    <g class="round-tag round-tag--outline">
      <circle class="ink-fill" cx="355" cy="147" r="92"/>
      <circle class="scallop-paper" cx="355" cy="147" r="78" stroke-width="14" stroke-dasharray="0 19.6"/>
      <circle class="brand-mark ink-fill" cx="355" cy="112" r="38"/>
      <text class="brand-name brand-name--ink brand-name--center" x="355" y="181">THE OTTERWRAP</text>
      <text class="brand-name brand-name--ink brand-name--center" x="355" y="196">COMPANY</text>
      <rect class="ink-fill" x="307" y="199" width="102" height="9"/>
      <text class="tagline tagline--round tagline--paper" x="358" y="206">Warm sleeping for young kids</text>
    </g>

    <g class="round-tag round-tag--outline">
      <circle class="ink-fill" cx="555" cy="145" r="92"/>
      <circle class="scallop-paper" cx="555" cy="145" r="78" stroke-width="14" stroke-dasharray="0 19.6"/>
      <circle class="brand-mark ink-fill" cx="555" cy="110" r="38"/>
      <text class="brand-name brand-name--ink brand-name--center" x="555" y="179">THE OTTERWRAP</text>
      <text class="brand-name brand-name--ink brand-name--center" x="555" y="194">COMPANY</text>
      <rect class="ink-fill" x="504" y="197" width="102" height="9"/>
      <text class="tagline tagline--round tagline--paper" x="555" y="204">Cálidos sueños, niños felices</text>
    </g>

    <g class="rect-label rect-label--outline">
      <rect class="ink-fill" x="663" y="87" width="277" height="123"/>
      <rect class="scallop-paper" x="678" y="100" width="247" height="97" stroke-width="10" stroke-dasharray="0 12.07"/>
      <text class="brand-name brand-name--soft brand-name--left" x="678" y="130">THE OTTERWRAP</text>
      <text class="brand-name brand-name--soft brand-name--left" x="678" y="147">COMPANY</text>
      <rect class="soft-fill" x="678" y="153" width="150" height="14"/>
      <text class="tagline tagline--rect tagline--paper" x="745" y="163">Cálidos sueños, niños felices</text>
      <circle class="brand-mark soft-fill" cx="875" cy="148" r="36"/>
    </g>

    <g class="round-tag round-tag--filled">
      <circle class="scallop-ink" cx="355" cy="358" r="80" stroke-width="20" stroke-dasharray="0 20.94"/>
      <circle class="brand-mark paper-fill" cx="355" cy="325" r="38"/>
      <text class="brand-name brand-name--paper brand-name--center" x="355" y="389">THE OTTERWRAP</text>
      <text class="brand-name brand-name--paper brand-name--center" x="355" y="404">COMPANY</text>
      <rect class="paper-fill" x="305" y="412" width="102" height="9"/>
      <text class="tagline tagline--round tagline--ink" x="356" y="419">Warm sleeping for young kids</text>
    </g>

    <g class="round-tag round-tag--filled">
      <circle class="scallop-ink" cx="555" cy="360" r="80" stroke-width="20" stroke-dasharray="0 20.94"/>
      <circle class="brand-mark paper-fill" cx="555" cy="327" r="38"/>
      <text class="brand-name brand-name--paper brand-name--center" x="555" y="391">THE OTTERWRAP</text>
      <text class="brand-name brand-name--paper brand-name--center" x="555" y="406">COMPANY</text>
      <rect class="paper-fill" x="504" y="413" width="102" height="9"/>
      <text class="tagline tagline--round tagline--ink" x="555" y="420">Cálidos sueños, niños felices</text>
    </g>

    <g class="rect-label rect-label--filled">
      <rect class="scallop-ink" x="676" y="306" width="251" height="105" stroke-width="12" stroke-dasharray="0 12.07"/>
      <text class="brand-name brand-name--paper brand-name--left" x="678" y="340">THE OTTERWRAP</text>
      <text class="brand-name brand-name--paper brand-name--left" x="678" y="357">COMPANY</text>
      <rect class="paper-fill" x="679" y="363" width="150" height="14"/>
      <text class="tagline tagline--rect tagline--ink" x="746" y="373">Cálidos sueños, niños felices</text>
      <circle class="brand-mark paper-fill" cx="875" cy="358" r="36"/>
    </g>
  </g>
</svg>
</body>
</html>
```